It's a new electrical company based in Newcastle NSW. I would like a logo between the two words "BRYN (insert logo) VOLT". I would like the logo to represent electrical and celtic style. For example I have seen a light bulb with a celtic pattern in the middle which looked very good. I would like it to be a white card, mainly black writing and quite basic not too much going on. But maybe have the logo partially red or green?

BRYN VOLT
Electrical Contractors
Domestic, commercial, fault finding, testing, re wires, switchboard upgrades
License No: 738421K
Fully Insured
Phone: 0431587720

```html
<!DOCTYPE html>
<html lang="en">
<head>
<meta charset="UTF-8">
<title>Bryn Volt – Business Card</title>
<link rel="stylesheet" href="https://fonts.googleapis.com/css2?family=Michroma&family=Oswald:wght@600&family=Open+Sans:wght@700&display=swap">
<style>
  :root {
    --backdrop: #e4e4e4;
    --card: #ffffff;
    --brand-red: #d01f27;
    --band-red: #c8141c;
    --band-highlight: #e0353c;
    --ink: #111111;
    --band-text: #ffffff;
  }
  html, body {
    margin: 0;
    padding: 0;
    width: 1200px;
    height: 900px;
    overflow: hidden;
    background: var(--backdrop);
  }
  .canvas {
    position: relative;
    width: 1200px;
    height: 900px;
  }
  .business-card {
    position: absolute;
    left: 100px;
    top: 150px;
    width: 1000px;
    height: 600px;
    background: var(--card);
    border-radius: 44px;
    box-shadow: 0 10px 30px rgba(0,0,0,0.12);
    overflow: hidden;
  }
  .brand-name {
    position: absolute;
    top: 140px;
    left: 0;
    width: 100%;
    display: flex;
    justify-content: center;
    align-items: center;
    gap: 34px;
    font-family: "Michroma", sans-serif;
    font-size: 84px;
    line-height: 1;
    color: var(--brand-red);
    letter-spacing: 4px;
  }
  .brand-mark {
    width: 70px;
    height: 70px;
    border-radius: 50%;
    background: var(--brand-red);
    flex: none;
  }
  .services-band {
    position: absolute;
    top: 312px;
    left: 0;
    width: 100%;
    height: 48px;
    background: var(--band-red);
    border-top: 3px solid var(--band-highlight);
    display: flex;
    align-items: center;
    justify-content: center;
    font-family: "Oswald", sans-serif;
    font-weight: 600;
    font-size: 29px;
    color: var(--band-text);
    letter-spacing: 0.3px;
  }
  .phone {
    position: absolute;
    top: 378px;
    left: 0;
    width: 100%;
    text-align: center;
    font-family: "Michroma", sans-serif;
    font-size: 42px;
    letter-spacing: 5px;
    color: var(--ink);
  }
  .licence,
  .insurance {
    position: absolute;
    left: 0;
    width: 100%;
    text-align: center;
    font-family: "Open Sans", sans-serif;
    font-weight: 700;
    color: var(--ink);
  }
  .licence {
    top: 448px;
    font-size: 24px;
  }
  .insurance {
    top: 482px;
    font-size: 28px;
  }
</style>
</head>
<body>
  <main class="canvas">
    <section class="business-card">
      <h1 class="brand-name">
        <span>BRYN</span>
        <span class="brand-mark" aria-hidden="true"></span>
        <span>VOLT</span>
      </h1>
      <div class="services-band">Domestic, commercial, fault finding, testing, re wires, switchboard upgrades</div>
      <p class="phone">0431587720</p>
      <p class="licence">License No: 738421K</p>
      <p class="insurance">Fully Insured</p>
    </section>
  </main>
</body>
</html>
```